DRAINWELL HOT WATER CYLINDER STICKER – PRINT LAYOUT

SECTION 1 – HOMEOWNER MAINTENANCE GUIDE (Boxed Section):
πŸ“– Hot Water Cylinder Maintenance
βœ… Monthly: Quick visual check for leaks, rust, or pooling water.
βœ… Every 6 Months: Test your TPR (Temperature & Pressure Relief) valve.
β€’ Lift the lever gently until water flows, then release.
β€’ If it’s blocked or constantly dripping – call us immediately.
βœ… Listen: Popping, banging, or rumbling? Could be sediment build-up.
βœ… Annually: Book a professional service to check anode, thermostat & valves.

SECTION 2 – WARNING SIGNS (Highlight Box or Red Accent):
🚨 Call Us Immediately If You Notice:
β€’ No hot water or inconsistent temperature
β€’ Water leaking from tank or pipes
β€’ Rust-coloured water
β€’ Sudden drop in water pressure

SECTION 3 – CALL TO ACTION (Large & Bold):
πŸ“ž NEED HELP FAST? CALL DRAINWELL FIRST!
πŸ“² PHONE: [0431 258 907] (largest text on sticker)
🌐 [www.drainwell.com.au]

FOOTER (Small Print):
Fully Licensed & Insured | HKTR 62840315 | 24/7 Emergency Service
This guide is for general maintenance only. For all repairs or safety concerns, contact a licensed plumber.

βœ… DESIGN RECOMMENDATIONS
β€’ Size: 27cm long x 10cm wide works well (large enough to read easily when standing).
β€’ Material: Waterproof vinyl with strong adhesive.
β€’ Colors:
o Header & Call-to-Action in your brand colors
o Maintenance guide in a light-shaded box for contrast
o Warning signs section with red accent or icon to grab attention
β€’ Icons: Use βœ… πŸ“– 🚨 πŸ“ž for quick scanning.

```html
<!DOCTYPE html>
<html lang="en">
<head>
<meta charset="utf-8">
<title>Drainwell Hot Water Cylinder Sticker – Print Layout</title>
<link rel="stylesheet" href="https://fonts.googleapis.com/css2?family=Barlow:wght@500;600;700&family=Barlow+Semi+Condensed:wght@600&family=Roboto:wght@400;500&display=swap">
<style>
  :root {
    --blue: #1a8ac6;
    --brown: #7b5331;
    --orange: #f15a2b;
    --charcoal: #58595b;
    --ink: #1d1d1b;
    --paper: #ffffff;
    --rule: #222;
  }
  html, body { margin: 0; padding: 0; width: 1200px; height: 1200px; overflow: hidden; background: var(--paper); }
  .stage { position: relative; width: 1050px; height: 1050px; transform: scale(1.142857); transform-origin: 0 0; font-family: "Roboto", Arial, sans-serif; color: var(--ink); }

  .dimension { position: absolute; }
  .dimension svg { display: block; overflow: visible; }
  .dimension-label { position: absolute; font-family: "Roboto", Arial, sans-serif; font-size: 21px; color: var(--ink); white-space: nowrap; }

  .sticker { position: absolute; left: 32px; width: 926px; height: 344px; box-sizing: border-box; border: 1.5px solid var(--rule); background: var(--paper); }
  .sticker--brown { --guide: var(--blue); --guide-sub: var(--charcoal); --warn-sub: var(--charcoal); --cta: var(--brown); --cta-lead: var(--orange); }
  .sticker--blue { --guide: var(--brown); --guide-sub: var(--blue); --warn-sub: #6f4a2a; --cta: var(--blue); --cta-lead: var(--blue); }

  /* maintenance guide */
  .guide { position: absolute; left: 15px; top: 14px; width: 538px; height: 224px; box-sizing: border-box; border: 2px solid var(--guide); overflow: hidden; }
  .guide-title { height: 30px; background: var(--guide); color: #fff; font-size: 19px; line-height: 30px; padding-left: 14px; letter-spacing: 0.2px; }
  .guide-sub { position: absolute; left: 11px; top: 37px; width: 340px; height: 22px; background: var(--guide-sub); color: #fff; font-size: 14px; font-weight: 500; line-height: 22px; padding-left: 28px; box-sizing: border-box; clip-path: polygon(0 0, 320px 0, 100% 100%, 0 100%); }
  .task { position: absolute; left: 11px; height: 20px; display: flex; align-items: center; white-space: nowrap; font-size: 15px; letter-spacing: -0.2px; }
  .task--tight { letter-spacing: -0.45px; }
  .tick { width: 17px; height: 17px; color: var(--blue); margin-right: 5px; flex: none; }
  .tag { background: var(--blue); color: #fff; font-size: 13px; font-weight: 500; letter-spacing: 0; height: 18px; line-height: 18px; padding: 0 12px 0 6px; margin-right: 5px; clip-path: polygon(0 0, calc(100% - 9px) 0, 100% 100%, 0 100%); }
  .step { position: absolute; left: 46px; height: 20px; display: flex; align-items: center; font-size: 15px; white-space: nowrap; letter-spacing: -0.2px; }
  .step::before { content: ""; width: 0; height: 0; border-left: 8px solid var(--blue); border-top: 5px solid transparent; border-bottom: 5px solid transparent; margin-right: 8px; }

  /* footer */
  .brand { position: absolute; left: 23px; top: 263px; display: flex; align-items: center; }
  .brand-dot { width: 34px; height: 34px; border-radius: 50%; background: var(--blue); margin-right: 10px; }
  .brand-name { font-family: "Barlow", Arial, sans-serif; font-weight: 700; font-size: 34px; color: var(--charcoal); letter-spacing: 0.5px; }
  .footer-divider { position: absolute; left: 283px; top: 248px; width: 2px; height: 81px; background: var(--brown); }
  .fine-print { position: absolute; left: 297px; top: 246px; width: 258px; font-size: 13px; line-height: 14.5px; letter-spacing: -0.15px; }
  .fine-print hr { border: 0; border-top: 1.5px solid var(--brown); margin: 5px 0 4px; }

  /* warning signs */
  .warning { position: absolute; left: 564px; top: 14px; width: 346px; height: 160px; box-sizing: border-box; border: 2px solid var(--orange); }
  .warning-head { position: absolute; left: -2px; top: -2px; width: 346px; height: 62px; }
  .warning-title { position: absolute; left: 12px; top: 5px; color: #fff; font-family: "Barlow", Arial, sans-serif; font-weight: 500; font-size: 21px; letter-spacing: 0.4px; }
  .warning-sub { position: absolute; left: 12px; top: 40px; color: #fff; font-size: 14.5px; font-weight: 500; line-height: 22px; }
  .sign { position: absolute; left: 20px; display: flex; align-items: center; font-size: 15px; white-space: nowrap; height: 20px; }
  .sign svg { width: 17px; height: 12px; margin-right: 7px; }

  /* call to action */
  .cta { position: absolute; left: 564px; top: 184px; width: 346px; height: 148px; box-sizing: border-box; border: 2px solid var(--cta); }
  .cta-title { height: 31px; background: var(--cta); color: #fff; font-family: "Barlow", Arial, sans-serif; font-weight: 500; font-size: 23px; letter-spacing: 2px; line-height: 32px; padding-left: 13px; }
  .cta-mark { position: absolute; left: 17px; top: 69px; width: 32px; height: 32px; border-radius: 50%; background: var(--cta); }
  .cta-divider { position: absolute; left: 66px; top: 36px; width: 2px; height: 98px; background: var(--brown); }
  .cta-lead { position: absolute; left: 80px; width: 250px; text-align: center; font-family: "Barlow", Arial, sans-serif; font-weight: 700; }
  .cta-lead--ask { top: 37px; color: var(--cta-lead); font-size: 15.5px; letter-spacing: 1.6px; }
  .cta-lead--call { top: 55px; color: var(--ink); font-size: 14.5px; letter-spacing: 0.3px; }
  .phone-row { position: absolute; left: 85px; top: 74px; display: flex; align-items: center; }
  .phone-icon { display: flex; flex-direction: column; align-items: center; margin-right: 9px; font-size: 7px; font-weight: 500; }
  .phone-icon svg { width: 16px; height: 14px; color: var(--orange); }
  .phone-number { font-family: "Barlow Semi Condensed", Arial Narrow, sans-serif; font-weight: 600; font-size: 39px; color: var(--orange); line-height: 40px; letter-spacing: 0.3px; }
  .web-row { position: absolute; left: 90px; top: 117px; display: flex; align-items: center; font-size: 16px; font-weight: 500; }
  .web-row svg { width: 19px; height: 19px; margin-right: 8px; color: var(--blue); }
</style>
</head>
<body>
<div class="stage">

  <div class="dimension" style="left:30px; top:69px;">
    <svg width="920" height="12"><g stroke="#333" stroke-width="1.5" fill="#333"><line x1="4" y1="6" x2="410" y2="6"/><line x1="510" y1="6" x2="916" y2="6"/><path d="M0 6l10-5v10z"/><path d="M920 6l-10-5v10z"/></g></svg>
    <span class="dimension-label" style="left:432px; top:-8px;">27cm</span>
  </div>
  <div class="dimension" style="left:994px; top:133px;">
    <svg width="12" height="344"><g stroke="#333" stroke-width="1.5" fill="#333"><line x1="6" y1="4" x2="6" y2="124"/><line x1="6" y1="220" x2="6" y2="340"/><path d="M6 0l-5 10h10z"/><path d="M6 344l-5-10h10z"/></g></svg>
    <span class="dimension-label" style="left:-26px; top:156px;">10 cm</span>
  </div>

  <section class="sticker sticker--brown" style="top:133px;">
    <div class="guide">
      <div class="guide-title">HOMEOWNER MAINTENANCE GUIDE</div>
      <div class="guide-sub">Hot Water Cylinder Maintenance</div>
      <div class="task" style="top:68px;"><svg class="tick" viewBox="0 0 17 17"><rect x="1" y="4" width="12" height="12" fill="none" stroke="currentColor" stroke-width="2"/><path d="M4 9l3 3 9-11" fill="none" stroke="currentColor" stroke-width="2.4"/></svg><span class="tag">Monthly:</span>Quick visual check for leaks, rust, or pooling water.</div>
      <div class="task" style="top:98px;"><svg class="tick" viewBox="0 0 17 17"><rect x="1" y="4" width="12" height="12" fill="none" stroke="currentColor" stroke-width="2"/><path d="M4 9l3 3 9-11" fill="none" stroke="currentColor" stroke-width="2.4"/></svg><span class="tag">Every 6 Months:</span>Test your TPR (Temperature &amp; Pressure Relief) valve.</div>
      <div class="step" style="top:120px;">Lift the lever gently until water flows, then release.</div>
      <div class="step" style="top:140px;">If it’s blocked or constantly dripping – call us immediately.</div>
      <div class="task" style="top:164px;"><svg class="tick" viewBox="0 0 17 17"><rect x="1" y="4" width="12" height="12" fill="none" stroke="currentColor" stroke-width="2"/><path d="M4 9l3 3 9-11" fill="none" stroke="currentColor" stroke-width="2.4"/></svg><span class="tag">Listen:</span>Popping, banging, or rumbling? Could be sediment build-up.</div>
      <div class="task task--tight" style="top:192px;"><svg class="tick" viewBox="0 0 17 17"><rect x="1" y="4" width="12" height="12" fill="none" stroke="currentColor" stroke-width="2"/><path d="M4 9l3 3 9-11" fill="none" stroke="currentColor" stroke-width="2.4"/></svg><span class="tag">Annually:</span>Book a professional service to check anode, thermostat &amp; valves.</div>
    </div>

    <div class="brand"><span class="brand-dot"></span><span class="brand-name">DRAINWELL</span></div>
    <div class="footer-divider"></div>
    <div class="fine-print">This guide is for general maintenance only. For all repairs or safety concerns, contact a licensed plumber.<hr>Fully Licensed &amp; Insured | HKTR 62840315 | 24/7 Emergency Service</div>

    <div class="warning">
      <svg class="warning-head" viewBox="0 0 346 62"><path d="M0 0H346V62H290L276 36H0Z" fill="var(--orange)"/><path d="M0 40H262L275 62H0Z" fill="var(--warn-sub)"/><path d="M314 9L333 43H295Z" fill="none" stroke="#fff" stroke-width="3" stroke-linejoin="round"/><rect x="312.6" y="20" width="2.8" height="13" fill="#fff"/><rect x="312.6" y="35.5" width="2.8" height="3" fill="#fff"/></svg>
      <div class="warning-title">WARNING SIGNS</div>
      <div class="warning-sub">Call Us Immediately If You Notice:</div>
      <div class="sign" style="top:68px;"><svg viewBox="0 0 17 12"><path d="M0 0l7 6-7 6zM8 0l8 6-8 6z" fill="var(--orange)"/></svg>No hot water or inconsistent temperature</div>
      <div class="sign" style="top:88px;"><svg viewBox="0 0 17 12"><path d="M0 0l7 6-7 6zM8 0l8 6-8 6z" fill="var(--orange)"/></svg>Water leaking from tank or pipes</div>
      <div class="sign" style="top:108px;"><svg viewBox="0 0 17 12"><path d="M0 0l7 6-7 6zM8 0l8 6-8 6z" fill="var(--orange)"/></svg>Rust-coloured water</div>
      <div class="sign" style="top:128px;"><svg viewBox="0 0 17 12"><path d="M0 0l7 6-7 6zM8 0l8 6-8 6z" fill="var(--orange)"/></svg>Sudden drop in water pressure</div>
    </div>

    <div class="cta">
      <div class="cta-title">CALL TO ACTION</div>
      <div class="cta-mark"></div>
      <div class="cta-divider"></div>
      <div class="cta-lead cta-lead--ask">NEED HELP FAST?</div>
      <div class="cta-lead cta-lead--call">CALL DRAINWELL FIRST!</div>
      <div class="phone-row"><span class="phone-icon"><svg viewBox="0 0 16 14"><path d="M1 4c0-3 14-3 14 0v2h-4V4H5v2H1z" fill="currentColor"/><rect x="3" y="7" width="10" height="7" rx="1" fill="currentColor"/></svg>PHONE</span><span class="phone-number">0431 258 907</span></div>
      <div class="web-row"><svg viewBox="0 0 20 20"><g fill="none" stroke="currentColor" stroke-width="1.6"><circle cx="10" cy="10" r="8.5"/><ellipse cx="10" cy="10" rx="3.8" ry="8.5"/><line x1="1.5" y1="10" x2="18.5" y2="10"/><line x1="3" y1="5.5" x2="17" y2="5.5"/><line x1="3" y1="14.5" x2="17" y2="14.5"/></g></svg>www.drainwell.com.au</div>
    </div>
  </section>

  <div class="dimension" style="left:30px; top:546px;">
    <svg width="920" height="12"><g stroke="#333" stroke-width="1.5" fill="#333"><line x1="4" y1="6" x2="410" y2="6"/><line x1="510" y1="6" x2="916" y2="6"/><path d="M0 6l10-5v10z"/><path d="M920 6l-10-5v10z"/></g></svg>
    <span class="dimension-label" style="left:432px; top:-8px;">27cm</span>
  </div>
  <div class="dimension" style="left:994px; top:610px;">
    <svg width="12" height="344"><g stroke="#333" stroke-width="1.5" fill="#333"><line x1="6" y1="4" x2="6" y2="124"/><line x1="6" y1="220" x2="6" y2="340"/><path d="M6 0l-5 10h10z"/><path d="M6 344l-5-10h10z"/></g></svg>
    <span class="dimension-label" style="left:-26px; top:156px;">10 cm</span>
  </div>

  <section class="sticker sticker--blue" style="top:610px;">
    <div class="guide">
      <div class="guide-title">HOMEOWNER MAINTENANCE GUIDE</div>
      <div class="guide-sub">Hot Water Cylinder Maintenance</div>
      <div class="task" style="top:68px;"><svg class="tick" viewBox="0 0 17 17"><rect x="1" y="4" width="12" height="12" fill="none" stroke="currentColor" stroke-width="2"/><path d="M4 9l3 3 9-11" fill="none" stroke="currentColor" stroke-width="2.4"/></svg><span class="tag">Monthly:</span>Quick visual check for leaks, rust, or pooling water.</div>
      <div class="task" style="top:98px;"><svg class="tick" viewBox="0 0 17 17"><rect x="1" y="4" width="12" height="12" fill="none" stroke="currentColor" stroke-width="2"/><path d="M4 9l3 3 9-11" fill="none" stroke="currentColor" stroke-width="2.4"/></svg><span class="tag">Every 6 Months:</span>Test your TPR (Temperature &amp; Pressure Relief) valve.</div>
      <div class="step" style="top:120px;">Lift the lever gently until water flows, then release.</div>
      <div class="step" style="top:140px;">If it’s blocked or constantly dripping – call us immediately.</div>
      <div class="task" style="top:164px;"><svg class="tick" viewBox="0 0 17 17"><rect x="1" y="4" width="12" height="12" fill="none" stroke="currentColor" stroke-width="2"/><path d="M4 9l3 3 9-11" fill="none" stroke="currentColor" stroke-width="2.4"/></svg><span class="tag">Listen:</span>Popping, banging, or rumbling? Could be sediment build-up.</div>
      <div class="task task--tight" style="top:192px;"><svg class="tick" viewBox="0 0 17 17"><rect x="1" y="4" width="12" height="12" fill="none" stroke="currentColor" stroke-width="2"/><path d="M4 9l3 3 9-11" fill="none" stroke="currentColor" stroke-width="2.4"/></svg><span class="tag">Annually:</span>Book a professional service to check anode, thermostat &amp; valves.</div>
    </div>

    <div class="brand"><span class="brand-dot"></span><span class="brand-name">DRAINWELL</span></div>
    <div class="footer-divider"></div>
    <div class="fine-print">This guide is for general maintenance only. For all repairs or safety concerns, contact a licensed plumber.<hr>Fully Licensed &amp; Insured | HKTR 62840315 | 24/7 Emergency Service</div>

    <div class="warning">
      <svg class="warning-head" viewBox="0 0 346 62"><path d="M0 0H346V62H290L276 36H0Z" fill="var(--orange)"/><path d="M0 40H262L275 62H0Z" fill="var(--warn-sub)"/><path d="M314 9L333 43H295Z" fill="none" stroke="#fff" stroke-width="3" stroke-linejoin="round"/><rect x="312.6" y="20" width="2.8" height="13" fill="#fff"/><rect x="312.6" y="35.5" width="2.8" height="3" fill="#fff"/></svg>
      <div class="warning-title">WARNING SIGNS</div>
      <div class="warning-sub">Call Us Immediately If You Notice:</div>
      <div class="sign" style="top:68px;"><svg viewBox="0 0 17 12"><path d="M0 0l7 6-7 6zM8 0l8 6-8 6z" fill="var(--orange)"/></svg>No hot water or inconsistent temperature</div>
      <div class="sign" style="top:88px;"><svg viewBox="0 0 17 12"><path d="M0 0l7 6-7 6zM8 0l8 6-8 6z" fill="var(--orange)"/></svg>Water leaking from tank or pipes</div>
      <div class="sign" style="top:108px;"><svg viewBox="0 0 17 12"><path d="M0 0l7 6-7 6zM8 0l8 6-8 6z" fill="var(--orange)"/></svg>Rust-coloured water</div>
      <div class="sign" style="top:128px;"><svg viewBox="0 0 17 12"><path d="M0 0l7 6-7 6zM8 0l8 6-8 6z" fill="var(--orange)"/></svg>Sudden drop in water pressure</div>
    </div>

    <div class="cta">
      <div class="cta-title">CALL TO ACTION</div>
      <div class="cta-mark"></div>
      <div class="cta-divider"></div>
      <div class="cta-lead cta-lead--ask">NEED HELP FAST?</div>
      <div class="cta-lead cta-lead--call">CALL DRAINWELL FIRST!</div>
      <div class="phone-row"><span class="phone-icon"><svg viewBox="0 0 16 14"><path d="M1 4c0-3 14-3 14 0v2h-4V4H5v2H1z" fill="currentColor"/><rect x="3" y="7" width="10" height="7" rx="1" fill="currentColor"/></svg>PHONE</span><span class="phone-number">0431 258 907</span></div>
      <div class="web-row"><svg viewBox="0 0 20 20"><g fill="none" stroke="currentColor" stroke-width="1.6"><circle cx="10" cy="10" r="8.5"/><ellipse cx="10" cy="10" rx="3.8" ry="8.5"/><line x1="1.5" y1="10" x2="18.5" y2="10"/><line x1="3" y1="5.5" x2="17" y2="5.5"/><line x1="3" y1="14.5" x2="17" y2="14.5"/></g></svg>www.drainwell.com.au</div>
    </div>
  </section>

</div>
</body>
</html>
```